Roofing Company Modern look

I want a modern and sophisticated look for our roofing business.

Our address is :

5172 Maple Crane Rd
Brookvale, Fl 39990

(555)-555-2719

www.SummitPeakRoofs.example

I also want to make sure on the back there is a spot to put
Project Manager Name :

Number:

Because the cards will be used by all sales people

Project Manager Name :

Also there are accreditation we have logos are uploaded here as well that I would like maybe on the back of card as well

I also want to highlight our special attributions or trades:

Residential & Commercial
Fully Insured
License # CCC8274916
Insurance Claims
Serving Central Florida Since 1992
Free Estimates

Contact Information for Business Card

Our address is :

5172 Maple Crane Rd
Brookvale, Fl 39990

(555)-555-2719

Project Manager Name :

Residential & Commercial
Fully Insured
License # CCC8274916
Insurance Claims
Free Estimates

Font styles to use
Serif
Sans Serif

Colors
3176b5

Requirements
Must have
• Must have royal blue like my logo grey and black are the colors I like

```html
<!DOCTYPE html>
<html lang="en">
<head>
<meta charset="utf-8">
<title>Summit Peak Roofing – Business Cards</title>
<link rel="stylesheet" href="https://fonts.googleapis.com/css2?family=Montserrat:wght@300;400;500;600;800&display=swap">
<style>
  :root {
    --stage: #066baf;
    --paper: #ffffff;
    --ink: #111111;
    --ink-soft: #2d2d2d;
    --royal: #3176b5;
    --royal-light: #4a8ccb;
    --sky: #5b9bd8;
    --badge-navy: #1d2a6b;
    --badge-grey: #e6e6e6;
  }
  * { margin: 0; padding: 0; box-sizing: border-box; }
  html, body { width: 1200px; height: 1200px; overflow: hidden; }
  body { background: var(--stage); position: relative; font-family: "Montserrat", sans-serif; }
  .card { position: absolute; width: 542px; height: 310px; box-shadow: 2px 3px 5px rgba(0,0,0,0.3); }
  .card svg { display: block; width: 100%; height: 100%; }
  .card--front-dark { left: 42px; top: 166px; }
  .card--back-dark { left: 612px; top: 166px; }
  .card--front-blue { left: 42px; top: 718px; }
  .card--back-blue { left: 612px; top: 718px; }
  .trade { font: 400 11px "Montserrat", sans-serif; fill: var(--paper); }
  .trade--strong { font-weight: 800; }
  .brand-name { font: 600 23px "Montserrat", sans-serif; fill: var(--royal); letter-spacing: 1px; }
  .brand-sub { font: 600 13px "Montserrat", sans-serif; fill: var(--royal); letter-spacing: 3px; }
  .address { font: 400 9px "Montserrat", sans-serif; fill: var(--ink-soft); }
  .website { font: 600 9px "Montserrat", sans-serif; fill: var(--ink); }
  .person { font: 800 43px "Montserrat", sans-serif; fill: var(--paper); }
  .role { font: 400 16px "Montserrat", sans-serif; fill: var(--paper); letter-spacing: 1.6px; }
  .phone { font: 300 16px "Montserrat", sans-serif; fill: var(--paper); letter-spacing: 0.8px; }
</style>
</head>
<body>

<svg width="0" height="0" style="position:absolute">
  <defs>
    <linearGradient id="dark-fill" x1="0" y1="1" x2="1" y2="0">
      <stop offset="0" stop-color="#333333"/>
      <stop offset="0.6" stop-color="#151515"/>
      <stop offset="1" stop-color="#0b0b0b"/>
    </linearGradient>
    <linearGradient id="blue-fill" x1="0" y1="1" x2="1" y2="0">
      <stop offset="0" stop-color="#4a8ccb"/>
      <stop offset="0.5" stop-color="#3677b8"/>
      <stop offset="1" stop-color="#2f6eae"/>
    </linearGradient>
  </defs>
</svg>

<!-- Front, dark variant -->
<div class="card card--front-dark">
  <svg viewBox="0 0 542 310">
    <rect width="542" height="310" fill="var(--paper)"/>
    <path d="M0 0 H303 Q200 165 0 171 Z" fill="var(--sky)"/>
    <path d="M0 0 H299 Q196 162 0 168 Z" fill="url(#dark-fill)"/>
    <text class="trade" x="18" y="28">Residential &amp; Commercial Fully Insure</text>
    <text class="trade" x="18" y="54">License # CCC8274916 Insurance Claims</text>
    <text class="trade" x="18" y="80">Serving Central Florida Since 1992</text>
    <text class="trade trade--strong" x="18" y="106">Free Estimates</text>
    <circle cx="394" cy="150" r="24" fill="var(--royal)"/>
    <text class="brand-name" x="394" y="212" text-anchor="middle">SUMMIT PEAK</text>
    <text class="brand-sub" x="394" y="238" text-anchor="middle">ROOFING INC.</text>
    <text class="address" x="258" y="286" text-anchor="middle">5172 Maple Crane Rd&#160;&#160;&#160;Brookvale, Fl&#160;&#160;&#160;39990(555)-555-2719</text>
    <text class="website" x="258" y="300" text-anchor="middle">www.SummitPeakRoofs.example</text>
  </svg>
</div>

<!-- Back, dark variant -->
<div class="card card--back-dark">
  <svg viewBox="0 0 542 310">
    <rect width="542" height="310" fill="url(#dark-fill)"/>
    <path d="M348 0 Q400 150 542 211 V0 Z" fill="var(--royal-light)"/>
    <path d="M351 0 Q403 146 542 207 V0 Z" fill="var(--paper)"/>
    <rect x="392" y="16" width="140" height="39" fill="var(--badge-grey)" stroke="var(--badge-navy)" stroke-width="1.5" role="img" aria-label="Authorized roofing contractor badge"/>
    <circle cx="515" cy="92" r="17" fill="var(--badge-grey)" stroke="#777" stroke-width="1.5" role="img" aria-label="Screened and approved badge"/>
    <rect x="502" y="136" width="29" height="39" fill="var(--badge-grey)" stroke="#2c5f8f" stroke-width="1.5" role="img" aria-label="Accredited business badge"/>
    <text class="person" x="22" y="151">John Smith</text>
    <text class="role" x="22" y="182">PROJECT MANAGER</text>
    <rect x="22" y="188" width="167" height="1.5" fill="var(--royal)"/>
    <text class="phone" x="22" y="261">+123 456 7890</text>
  </svg>
</div>

<!-- Front, blue variant -->
<div class="card card--front-blue">
  <svg viewBox="0 0 542 310">
    <rect width="542" height="310" fill="var(--paper)"/>
    <path d="M0 0 H303 Q200 165 0 171 Z" fill="var(--ink)"/>
    <path d="M0 0 H299 Q196 162 0 168 Z" fill="url(#blue-fill)"/>
    <text class="trade" x="18" y="28">Residential &amp; Commercial Fully Insure</text>
    <text class="trade" x="18" y="54">License # CCC8274916 Insurance Claims</text>
    <text class="trade" x="18" y="80">Serving Central Florida Since 1992</text>
    <text class="trade trade--strong" x="18" y="106">Free Estimates</text>
    <circle cx="394" cy="150" r="24" fill="var(--royal)"/>
    <text class="brand-name" x="394" y="212" text-anchor="middle">SUMMIT PEAK</text>
    <text class="brand-sub" x="394" y="238" text-anchor="middle">ROOFING INC.</text>
    <text class="address" x="258" y="286" text-anchor="middle">5172 Maple Crane Rd&#160;&#160;&#160;Brookvale, Fl&#160;&#160;&#160;39990(555)-555-2719</text>
    <text class="website" x="258" y="300" text-anchor="middle">www.SummitPeakRoofs.example</text>
  </svg>
</div>

<!-- Back, blue variant -->
<div class="card card--back-blue">
  <svg viewBox="0 0 542 310">
    <rect width="542" height="310" fill="url(#blue-fill)"/>
    <path d="M348 0 Q400 150 542 211 V0 Z" fill="var(--ink)"/>
    <path d="M351 0 Q403 146 542 207 V0 Z" fill="var(--paper)"/>
    <rect x="392" y="16" width="140" height="39" fill="var(--badge-grey)" stroke="var(--badge-navy)" stroke-width="1.5" role="img" aria-label="Authorized roofing contractor badge"/>
    <circle cx="515" cy="92" r="17" fill="var(--badge-grey)" stroke="#777" stroke-width="1.5" role="img" aria-label="Screened and approved badge"/>
    <rect x="502" y="136" width="29" height="39" fill="var(--badge-grey)" stroke="#2c5f8f" stroke-width="1.5" role="img" aria-label="Accredited business badge"/>
    <text class="person" x="22" y="151">John Smith</text>
    <text class="role" x="22" y="182">PROJECT MANAGER</text>
    <rect x="22" y="188" width="167" height="1.5" fill="var(--sky)"/>
    <text class="phone" x="22" y="261">+123 456 7890</text>
  </svg>
</div>

</body>
</html>
```